Looking for a cool, modern Cannabis Jar Label

I want you to come up with a better, modern look for a label.

I need it sized to 4” x 3” - I plan to print directly to label printer.

I want you to use Photoshop and deliver me a layered PSD file that I can edit and modify the information as needed..

The label information will need to include places for:
(1) Strain Name - most important part of label - larger font size than rest - example Marlow Frost, KTV #7, Copperleaf Haze
(2) Pricing - for Gram, 1/8, 1/4, 1/2. and Ounce
(3) Strain Designation (Hybrid, Indica or Sativa) - maybe color coded, different color for Indica v. Sativa, just an idea
(4) THC and CBD percentages - for example 23% THC and 0.05% CBD
(5) Farm name - a place where we can add the name/logo of the business that produced the product. example - Bramwell Farms

I have attached a simple mockup showing the information.

I have also attached a few samples of labels we like to give you an idea of the look and feel we are going for.

I am wanting a very clean, modern, classy, readable look.The font will use is Gotham Font.

HI Everyone! Thank you for all of your designs. I am requesting an extension because I need more time to give adequate feedback to the designers. Thank you for your participation and all of your efforts! I will be making a decision soon!

• Gotham Font

Designer to choose colors to be used in the design.

• Thank you for your designs. I am sorry i have been slow in providing feedback, things have been really busy around here!
• I wanted to give some group general feedback. After reviewing all of the designs, there is a common theme among all of the designs that I would like to see changed.
• I would like to see the per gram pricing more prominent on the label. This is what most people are looking for when they are purchasing the product. So I would like to see this stand out from the other pricing tiers. As I think about it, they don't all need to be grouped together in a line. You could have the Per Gram pricing front and center some where and then the other pricing tiers grouped together somewhere else on the label.
• This is the order of importance of items on the label. Items at the the top of the list should be bigger than those below it.
• 1. Strain name
• 2. Pricing - being per gram the most important of all prices
• 3. THC/CBD percentages
• 4. Strain Type (indica, sativa, hybrid)
• 5. Farm name/logo
• When laying out these labels, they will be going on rounded jars and they will be on display. Think of jars with fancy labels in a candy store. They need to be eye catchy, appealing, but easy read.
• Thank you for all of your hard work, everyone is doing a great job.
• Best,
• Nadia

```html
<!DOCTYPE html>
<html lang="en">
<head>
<meta charset="utf-8">
<title>Alder Bay Frost – Jar Labels</title>
<link href="https://fonts.googleapis.com/css2?family=Saira:wght@300;400;600;700&display=swap" rel="stylesheet">
<style>
  :root {
    --ink: #15191a;
    --band: #161a1b;
    --price-text: #e8ece6;
    --dot: #6ebe45;
    --sativa-a: #cfdc9e;
    --sativa-b: #4acd00;
    --hybrid-a: #cddb9c;
    --hybrid-b: #c3e024;
    --indica-a: #cadaa2;
    --indica-b: #5c9e3d;
  }
  * { margin: 0; padding: 0; box-sizing: border-box; }
  html, body { width: 1200px; height: 1200px; overflow: hidden; }
  body {
    position: relative;
    font-family: "Saira", "Arial", sans-serif;
    color: var(--ink);
    background:
      radial-gradient(ellipse 380px 520px at 170px 260px, #a2d168 0%, transparent 70%),
      radial-gradient(ellipse 360px 420px at 200px 920px, #bccc74 0%, transparent 70%),
      radial-gradient(ellipse 420px 360px at 1100px 380px, #7aa33a 0%, transparent 70%),
      radial-gradient(ellipse 360px 340px at 1120px 1000px, #6a9a4a 0%, transparent 70%),
      radial-gradient(ellipse 300px 260px at 1000px 700px, #263424 0%, transparent 75%),
      linear-gradient(90deg, #7ca452 0%, #5a6e3c 45%, #2f3d2c 75%, #425a34 100%);
  }
  .label {
    position: absolute;
    left: 390px;
    width: 500px;
    height: 375px;
  }
  .label--sativa { top: 18px; --a: var(--sativa-a); --b: var(--sativa-b); }
  .label--hybrid { top: 413px; --a: var(--hybrid-a); --b: var(--hybrid-b); }
  .label--indica { top: 808px; --a: var(--indica-a); --b: var(--indica-b); }

  .label__head, .label__body {
    background: linear-gradient(155deg, var(--a) 0%, var(--b) 100%);
    position: relative;
  }
  .label__head { height: 128px; }
  .strain-name {
    position: absolute;
    left: 32px;
    top: 26px;
    font-weight: 700;
    font-size: 40px;
    line-height: 42px;
    letter-spacing: 0.5px;
    text-transform: uppercase;
  }
  .price-band {
    height: 66px;
    background: var(--band);
    display: flex;
    align-items: center;
    justify-content: center;
    gap: 10px;
    color: var(--price-text);
    font-weight: 600;
    font-size: 30px;
    letter-spacing: 0.5px;
  }
  .price-band .dot {
    width: 6px; height: 6px; border-radius: 50%;
    background: var(--dot);
    flex: none;
  }
  .price sup { font-size: 10px; vertical-align: 16px; margin-left: 1px; }
  .label__body { height: 181px; }
  .strain-type {
    position: absolute;
    left: 32px;
    top: 25px;
    font-weight: 700;
    font-size: 39px;
    line-height: 40px;
  }
  .potency {
    position: absolute;
    left: 32px;
    top: 66px;
    font-weight: 300;
    font-size: 28px;
    line-height: 29px;
  }
  .potency .row { display: flex; }
  .potency .pct { width: 57px; }
  .potency sup { font-size: 14px; vertical-align: 12px; }
  .farm-mark {
    position: absolute;
    left: 179px;
    top: 29px;
    width: 287px;
    height: 127px;
    background: var(--ink);
    box-shadow: 0 1px 3px rgba(0,0,0,0.35);
  }
</style>
</head>
<body>

  <section class="label label--sativa">
    <div class="label__head"><h1 class="strain-name">Alder Bay<br>Frost</h1></div>
    <div class="price-band">
      <span class="dot"></span><span class="price">10<sup>$</sup></span>
      <span class="dot"></span><span class="price">35<sup>$</sup></span>
      <span class="dot"></span><span class="price">70<sup>$</sup></span>
      <span class="dot"></span><span class="price">140<sup>$</sup></span>
      <span class="dot"></span><span class="price">280<sup>$</sup></span>
      <span class="dot"></span>
    </div>
    <div class="label__body">
      <h2 class="strain-type">SATIVA</h2>
      <div class="potency">
        <div class="row"><span class="pct">28<sup>%</sup></span><span>THC</span></div>
        <div class="row"><span class="pct">2<sup>%</sup></span><span>CBD</span></div>
      </div>
      <div class="farm-mark" role="img" aria-label="Farm name or logo area"></div>
    </div>
  </section>

  <section class="label label--hybrid">
    <div class="label__head"><h1 class="strain-name">Alder Bay<br>Frost</h1></div>
    <div class="price-band">
      <span class="dot"></span><span class="price">10<sup>$</sup></span>
      <span class="dot"></span><span class="price">35<sup>$</sup></span>
      <span class="dot"></span><span class="price">70<sup>$</sup></span>
      <span class="dot"></span><span class="price">140<sup>$</sup></span>
      <span class="dot"></span><span class="price">280<sup>$</sup></span>
      <span class="dot"></span>
    </div>
    <div class="label__body">
      <h2 class="strain-type">HYBRID</h2>
      <div class="potency">
        <div class="row"><span class="pct">28<sup>%</sup></span><span>THC</span></div>
        <div class="row"><span class="pct">2<sup>%</sup></span><span>CBD</span></div>
      </div>
      <div class="farm-mark" role="img" aria-label="Farm name or logo area"></div>
    </div>
  </section>

  <section class="label label--indica">
    <div class="label__head"><h1 class="strain-name">Alder Bay<br>Frost</h1></div>
    <div class="price-band">
      <span class="dot"></span><span class="price">10<sup>$</sup></span>
      <span class="dot"></span><span class="price">35<sup>$</sup></span>
      <span class="dot"></span><span class="price">70<sup>$</sup></span>
      <span class="dot"></span><span class="price">140<sup>$</sup></span>
      <span class="dot"></span><span class="price">280<sup>$</sup></span>
      <span class="dot"></span>
    </div>
    <div class="label__body">
      <h2 class="strain-type">INDICA</h2>
      <div class="potency">
        <div class="row"><span class="pct">28<sup>%</sup></span><span>THC</span></div>
        <div class="row"><span class="pct">2<sup>%</sup></span><span>CBD</span></div>
      </div>
      <div class="farm-mark" role="img" aria-label="Farm name or logo area"></div>
    </div>
  </section>

</body>
</html>
```